Enhance the web site presence of KRU Global Limited

Upgrade the current web site www.krucircuit-example.com to share with the audience our current plan and future developments of our company. I have created a worksheet which shows all the pages that I like to have. The home page in English, Japanese and Chinese is hyperlinked to the various pages. Under the product, we should allow the user to select "single sided PCB or double sided PCB". The translation of the contents of the pages with Japanese is not complete but the English and Chinese are complete. You can download the briefing and photos in the dropbox files below;

https://www.filebinvault-example.com/sh/x7k2mq9plw4rt8a/BBQZ_Hn462UdgnRtYmXzzYfLb?dl=0

Target Market(s)

Electronic companies

Industry/Entity Type

Electronic

Coding

Coded - Design and coding required

Number of Pages Required

5+ page

Font styles to use
Sans Serif

Colors
00a990
0353a1
33b8a4

Requirements
Must have
• Get a sense of confidence on our company's integrity and capability to deliver the highest quality PCBs with the most competitive prices and best services. A sense of elegance is essential as we DON'T treat profits as the number one goal. Our number goal is to do the RIGHT things right. Having a mixture of our company photos will be appropriate.

```html
<!DOCTYPE html>
<html lang="en">
<head>
<meta charset="utf-8">
<title>KRU Global Limited – Printed Circuit Boards</title>
<link href="https://fonts.googleapis.com/css2?family=Lato:wght@300;400;700&family=Roboto:wght@300;400;500&display=swap" rel="stylesheet">
<style>
:root{
  --green:#0f8a5c;
  --green-dark:#0b6e48;
  --green-deep:#095c3c;
  --teal:#00a990;
  --teal-light:#33b8a4;
  --blue:#2ba3c9;
  --orange:#e8951f;
  --ink:#333;
  --muted:#777;
  --line:#e4e4e4;
  --paper:#fff;
  --backdrop:#f6f6f6;
}
*{box-sizing:border-box;margin:0;padding:0}
html,body{width:682px;height:1200px;overflow:hidden}
body{background:var(--backdrop);font-family:"Lato",sans-serif;color:var(--ink);position:relative}
.page{position:absolute;left:48px;top:25px;width:587px;height:1152px;background:var(--paper);box-shadow:0 0 8px rgba(0,0,0,.12);overflow:hidden}
.abs{position:absolute}

/* header */
.topbar{left:180px;top:0;width:407px;height:22px;background:#f1f1f1;clip-path:polygon(0 0,100% 0,100% 100%,14px 100%)}
.topbar-item{top:6px;font-size:6.5px;color:#555;display:flex;align-items:center;gap:4px}
.lang{left:490px;top:3px;width:64px;height:15px;border:1px solid #ddd;background:#fff;font-size:5px;color:#666;display:flex;align-items:center;padding-left:6px;gap:4px}
.lang .flag{width:8px;height:6px;background:#c9d3e6;border-radius:1px}
.lang .caret{margin-left:auto;width:13px;height:100%;border-left:1px solid #ddd;display:flex;align-items:center;justify-content:center}
.brand{left:32px;top:22px;font-family:"Roboto",sans-serif;font-weight:500;font-size:28px;letter-spacing:3px;color:var(--green-deep);line-height:1}
.nav{top:42px;left:0;width:587px;font-family:"Roboto",sans-serif;font-size:6.5px;color:#666}
.nav a{position:absolute;text-decoration:none;color:inherit}
.nav a.active{color:var(--green);font-weight:500}

/* hero */
.hero{left:0;top:72px;width:587px;height:288px;background:linear-gradient(110deg,#2aa7cf 0%,#1ea3b0 40%,#13966f 75%,#0f8d5c 100%);border-top:3px solid var(--teal-light)}
.field{color:#eaf6f8;font-size:7px;border-bottom:1px solid rgba(255,255,255,.55);width:88px;padding-bottom:4px}
.message{left:76px;top:198px;width:192px;height:42px;background:rgba(255,255,255,.2);font-size:6.5px;color:#eef;padding:10px 11px}
.btn-orange{left:76px;top:253px;width:65px;height:19px;border-radius:10px;background:var(--orange);color:#fff;font-size:6.5px;display:flex;align-items:center;justify-content:center}
.hero-title{left:317px;top:137px;color:#fff;font-family:"Roboto",sans-serif;font-weight:300;font-size:11.5px;line-height:17px}
.hero-title strong{font-weight:500;font-size:15px;letter-spacing:3.5px}
.checks{left:322px;top:183px;list-style:none;color:#fff;font-size:7.5px}
.checks li{height:15.3px;display:flex;align-items:center;gap:6px}
.btn-ghost{left:321px;top:263px;width:73px;height:22px;border:1.5px solid var(--teal-light);border-radius:11px;color:var(--teal-light);font-size:6.5px;display:flex;align-items:center;justify-content:center}
.slider-tab{left:263px;top:348px;width:60px;height:12px;background:#fff;clip-path:polygon(14% 0,86% 0,100% 100%,0 100%)}
.dots{left:280px;top:350px;display:flex;gap:4px}
.dots i{width:5px;height:5px;border-radius:50%;border:1px solid var(--green)}
.dots i.on{background:var(--green)}

/* services */
.badge{width:48px;height:48px;border-radius:50%;background:#fff;box-shadow:0 2px 6px rgba(0,0,0,.18);display:flex;align-items:center;justify-content:center}
.badge span{width:36px;height:36px;border-radius:50%;background:var(--teal-light)}
.service{width:240px;text-align:center}
.service h3{font-family:"Roboto",sans-serif;font-weight:400;font-size:10px;line-height:12px;color:#222;text-transform:uppercase}
.service p{margin-top:8px;font-size:7px;line-height:11px;color:var(--muted)}
.btn-outline{margin:11px auto 0;width:70px;height:19px;border:1px solid var(--teal-light);border-radius:10px;color:var(--teal);font-size:6.5px;display:flex;align-items:center;justify-content:center}

.divider{left:0;top:546px;width:587px;height:1px;background:var(--line)}
.divider-mark{left:273px;top:541px;width:40px;background:#fff;text-align:center;font-family:"Roboto",sans-serif;font-size:8px;letter-spacing:1px;color:#bbb}
.section-title{left:0;width:587px;text-align:center;font-family:"Roboto",sans-serif;font-size:15px;color:#222}
.underline{left:284px;top:604px;width:18px;height:2px;background:var(--green)}

/* news */
.photo{display:block}
.news-overlay{left:58px;top:729px;width:108px;height:71px;background:rgba(11,125,80,.94);color:#fff;padding:11px 12px}
.news-overlay h4{font-size:5.5px;font-weight:400}
.news-overlay p{font-size:6.5px;line-height:8px;margin-top:9px}
.news-overlay .more{font-size:5px;margin-top:9px}
.news-card{border:1px solid #e6e6e6;background:#fff}
.news-text{position:absolute;width:120px}
.news-text h4{font-size:6.5px;font-weight:400;color:#333}
.news-text h4::after{content:"";display:block;width:10px;height:1.5px;background:var(--green);margin-top:5px}
.news-text p{font-size:6px;line-height:8px;color:#888;margin-top:6px}
.news-text .more{font-size:5px;color:#555;margin-top:10px;padding-left:3px}
.news-text .more b{color:var(--green);font-weight:400}

/* customers */
.cust-line{top:862px;height:1px;background:var(--line)}
.client{top:903px;height:24px;display:flex;align-items:center;justify-content:center;font-family:"Roboto",sans-serif;font-weight:500;font-size:14px}
.arrow{top:906px;color:#bbb;font-size:16px;font-weight:300}

/* footer */
.footer{left:0;top:962px;width:587px;height:163px;background:var(--green)}
.footer-base{left:0;top:1125px;width:587px;height:27px;background:var(--green-deep);color:rgba(255,255,255,.4);font-size:6.5px;padding:10px 0 0 49px}
.f-head{top:998px;font-family:"Roboto",sans-serif;font-weight:300;font-size:9.5px;color:rgba(255,255,255,.35)}
.f-links{left:44px;top:1018px;list-style:none;color:#fff;font-size:6.5px;line-height:11.5px}
.f-contact{left:153px;color:#fff;font-size:6.5px;line-height:8px;display:flex;gap:8px}
.f-contact .ico{width:11px;height:11px;border-radius:50%;background:var(--green-dark);flex:none;display:flex;align-items:center;justify-content:center}
.social{top:1018px;width:15px;height:15px;border-radius:50%;background:var(--green-deep)}
.map{left:411px;top:1013px;width:133px;height:81px;background:linear-gradient(135deg,#e9f2ef,#cfe1da)}
</style>
</head>
<body>
<div class="page">

  <header>
    <div class="abs topbar"></div>
    <div class="abs topbar-item" style="left:218px">
      <svg width="7" height="7" viewBox="0 0 10 10"><path d="M2 1l2 2-1 1.5a6 6 0 0 0 2.5 2.5L7 6l2 2-1.2 1.5C4.5 9 1 5.5.5 2.2z" fill="#555"/></svg>
      <span style="color:#333">(852) 2460 9183</span>
    </div>
    <div class="abs topbar-item" style="left:306px">
      <svg width="7" height="6" viewBox="0 0 10 8"><rect x="0" y="0" width="10" height="8" fill="#888"/><path d="M0 0l5 4 5-4" stroke="#fff" fill="none"/></svg>
      <span>sales@krucircuit-example.com</span>
    </div>
    <div class="abs lang">ENGLISH <span class="flag"></span><span class="caret">⌄</span></div>
    <div class="abs brand">KRU</div>
    <nav class="abs nav">
      <a class="active" style="left:287px;top:24px">HOME</a>
      <a style="left:326px;top:24px">PRODUCTS</a>
      <a style="left:380px;top:24px">TECHNICAL CAPABILITIES</a>
      <a style="left:483px;top:24px">NEWS</a>
      <a style="left:519px;top:24px">CONTACT</a>
    </nav>
  </header>

  <section class="abs hero" role="img" aria-label="Teal to green banner with faint circuit board traces">
  </section>
  <form class="hero-form">
    <div class="abs field" style="left:76px;top:146px">Name</div>
    <div class="abs field" style="left:180px;top:146px">Email</div>
    <div class="abs field" style="left:76px;top:168px">Phone</div>
    <div class="abs field" style="left:180px;top:169px">Subject</div>
    <div class="abs message">Enter your message</div>
    <div class="abs btn-orange">CONTACT US</div>
  </form>
  <h1 class="abs hero-title">OUR PRINTED CIRCUIT BOARD BUSINESS IS<br>COMMITTED TO <strong>“EXCELLENCE”</strong></h1>
  <ul class="abs checks">
    <li><svg width="7" height="6" viewBox="0 0 8 6"><path d="M1 3l2 2 4-4" stroke="#fff" stroke-width="1.3" fill="none"/></svg>Excellence in Quality</li>
    <li><svg width="7" height="6" viewBox="0 0 8 6"><path d="M1 3l2 2 4-4" stroke="#fff" stroke-width="1.3" fill="none"/></svg>Excellence in Prices</li>
    <li><svg width="7" height="6" viewBox="0 0 8 6"><path d="M1 3l2 2 4-4" stroke="#fff" stroke-width="1.3" fill="none"/></svg>Excellence in Services</li>
    <li><svg width="7" height="6" viewBox="0 0 8 6"><path d="M1 3l2 2 4-4" stroke="#fff" stroke-width="1.3" fill="none"/></svg>Excellence in on time delivery</li>
  </ul>
  <div class="abs btn-ghost">READ MORE</div>
  <div class="abs slider-tab"></div>
  <div class="abs dots"><i class="on"></i><i></i><i></i></div>

  <div class="abs badge" style="left:143px;top:340px"><span role="img" aria-label="Single layer circuit icon"></span></div>
  <div class="abs badge" style="left:396px;top:340px"><span role="img" aria-label="Multi layer circuit icon"></span></div>

  <section class="abs service" style="left:47px;top:405px">
    <h3>Single layered printed<br>circuit boards</h3>
    <p>We are offering single layered circuit boards through our own production facility in China for customers in the audio and video industry, home appliance and camera...</p>
    <div class="btn-outline">LEARN MORE</div>
  </section>
  <section class="abs service" style="left:300px;top:405px">
    <h3>Double layered &amp; multi-layered<br>printed circuit boards</h3>
    <p>We are offering two layered and multi-layered circuit boards for our customers through our strategically approved printed circuit boards manufacturers...</p>
    <div class="btn-outline">LEARN MORE</div>
  </section>

  <div class="abs divider"></div>
  <div class="abs divider-mark">KRU</div>

  <h2 class="abs section-title" style="top:581px">LATEST NEWS</h2>
  <div class="abs underline"></div>

  <div class="abs photo" style="left:67px;top:639px;width:227px;height:169px;background:linear-gradient(160deg,#1b2a22,#2f5a40 55%,#6d8a70)" role="img" aria-label="Close-up of a green circuit board with chips"></div>
  <div class="abs news-overlay">
    <h4>LOREM LIPSUM</h4>
    <p>Lorem Ipsum is simply dummy text of the printing.</p>
    <div class="more">READ MORE &nbsp;›</div>
  </div>

  <div class="abs news-card" style="left:308px;top:639px;width:216px;height:81px"></div>
  <div class="abs photo" style="left:440px;top:639px;width:84px;height:81px;background:linear-gradient(135deg,#0a1f6e,#1f7fd6 55%,#55d7e8)" role="img" aria-label="Glowing blue microchip on a circuit board"></div>
  <div class="news-text" style="left:325px;top:655px">
    <h4>LOREM LIPSUM</h4>
    <p>Lorem Ipsum is simply dummy<br>text of the printing.</p>
    <div class="more">READ MORE &nbsp;<b>›</b></div>
  </div>

  <div class="abs news-card" style="left:308px;top:726px;width:216px;height:82px"></div>
  <div class="abs photo" style="left:308px;top:726px;width:83px;height:82px;background:linear-gradient(135deg,#d9dde0,#9aa3ab 60%,#40474f)" role="img" aria-label="Office worker using a laptop"></div>
  <div class="news-text" style="left:409px;top:742px">
    <h4>LOREM LIPSUM</h4>
    <p>Lorem Ipsum is simply dummy<br>text of the printing.</p>
    <div class="more">READ MORE &nbsp;<b>›</b></div>
  </div>

  <div class="abs cust-line" style="left:0;width:208px"></div>
  <div class="abs cust-line" style="left:378px;width:209px"></div>
  <h2 class="abs section-title" style="top:855px">OUR CUSTOMERS</h2>
  <div class="abs arrow" style="left:45px">‹</div>
  <div class="abs client" style="left:72px;width:80px;color:#999;font-size:10px">NORVANE</div>
  <div class="abs client" style="left:166px;width:80px;color:#e2231a">KELMORA</div>
  <div class="abs client" style="left:268px;width:60px;color:#1d3e8a">OSTRIX</div>
  <div class="abs client" style="left:354px;width:78px;color:#c8102e;font-size:16px">DRAVEL</div>
  <div class="abs client" style="left:455px;width:62px;color:#333;font-size:10px">Lumora</div>
  <div class="abs arrow" style="left:536px">›</div>

  <footer>
    <div class="abs footer"></div>
    <div class="abs f-head" style="left:43px">QUICK LINKS</div>
    <div class="abs f-head" style="left:153px">CONTACT US</div>
    <div class="abs f-head" style="left:307px">FOLLOW US</div>
    <div class="abs f-head" style="left:410px">OUR LOCATION</div>
    <ul class="abs f-links">
      <li>Home</li><li>Products</li><li>Technical Capabilities</li><li>News</li><li>Contact Us</li>
    </ul>
    <div class="abs f-contact" style="top:1017px">
      <span class="ico"><svg width="5" height="6" viewBox="0 0 6 8"><path d="M3 0a3 3 0 0 1 3 3c0 2-3 5-3 5S0 5 0 3a3 3 0 0 1 3-3z" fill="#fff"/></svg></span>
      <span>18/F Harbour Point 27 Marsh Road<br>Wan Chai, HONG KONG</span>
    </div>
    <div class="abs f-contact" style="top:1040px">
      <span class="ico"><svg width="5" height="5" viewBox="0 0 10 10"><path d="M2 1l2 2-1 1.5a6 6 0 0 0 2.5 2.5L7 6l2 2-1.2 1.5C4.5 9 1 5.5.5 2.2z" fill="#fff"/></svg></span>
      <span><i>CALL US</i><br>(852)24609183</span>
    </div>
    <div class="abs f-contact" style="top:1064px">
      <span class="ico"><svg width="5" height="4" viewBox="0 0 10 8"><rect width="10" height="8" fill="#fff"/></svg></span>
      <span style="padding-top:2px">sales@krucircuit-example.com</span>
    </div>
    <div class="abs social" style="left:308px"></div>
    <div class="abs social" style="left:328px"></div>
    <div class="abs social" style="left:347px"></div>
    <div class="abs map" role="img" aria-label="Street map showing the office location"></div>
    <div class="abs footer-base">© 2017 krucircuit. All Rights Reserved</div>
  </footer>

</div>
</body>
</html>
```